German Auto Restoration Website Design

We are working with a Classic Car Restoration company in California.
They compete with guys like this:
https://torvexautorestoration.com

We could not find any auto restoration company websites for inspiration. We attached some images of the type of work they do.

Thank you for taking the time to consider designing a website for us. We are web developers based in Stockton, CA, USA. Most of our projects go through the same process. Understanding this process may help you win a project with us. We custom-code all of our websites in-house. We don’t have any requirements as to what tools you use for your design, but we ask that you follow these guidelines.

IMAGES:
If you use any images or icons in the design, we ask that you have a link to the asset so we can purchase the image/icon. Most of the designs we submit do not have the customer’s images on them unless they have some great images. Be creative; show us the feeling you are trying to portray with your image choices. Use any royalty-free site you choose. We subscribe to Qinto and mainly use their images, but we can purchase images outside of Qinto. PLEASE NOTE: we will not submit designs to clients with watermarks on the images.

FONTS:
We ask that you identify the fonts you’re using in the design. This can be done in a message if you want. We typically use Plexa Fonts and Qinto Fonts.

CONTENT:
We're always open to different content and ideas. We often submit designs with stock images so the client can see our vision. We typically take pictures after the website launch to use their images with our vision. Lorem Ipsum is fine for paragraphs, but we ask that you make the Headers with correct English. We want to be able to show the vision and identify the sections of the website.

INSPIRATION:
We typically add a couple of links in the brief of websites we like to help you get started in your design.

REVISIONS:
We do not often ask for revisions of the designs unless we see something in the design that may not appeal to the client. If there are slight changes that we want to make, we do that in the development process.

FEEDBACK:
We rarely give feedback on designs during the design process. We are working on many website projects and do not have the time to provide feedback. We usually respond if your request is well thought out and asks specific questions, but a note asking “feedback, please” usually goes unanswered.

```html
<!DOCTYPE html>
<html lang="en">
<head>
<meta charset="utf-8">
<title>Kessler Restorations</title>
<link href="https://fonts.googleapis.com/css2?family=Poppins:wght@400;500;600;700&display=swap" rel="stylesheet">
<style>
:root{
  --red:#e8322b;
  --yellow:#fce21b;
  --black:#111111;
  --dark:#3a3a3a;
  --grey:#e6e4e4;
  --text:#333333;
  --white:#ffffff;
}
*{margin:0;padding:0;box-sizing:border-box}
html,body{width:1200px;height:4374px;overflow:hidden}
body{font-family:'Poppins',sans-serif;color:var(--text);background:var(--white);position:relative}
section,header,footer{position:relative;width:1200px;overflow:hidden}
.abs{position:absolute}
.ph{position:absolute}
.tag{display:inline-block;font-size:12px;letter-spacing:.5px;padding:6px 0;text-align:center;clip-path:polygon(6% 0,100% 0,94% 100%,0 100%)}
.tag-yellow{background:var(--yellow);color:#fff}
.tag-black{background:var(--black);color:#fff}
.tag-red{background:var(--red);color:#fff}
.sec-title{font-size:27px;font-weight:700;color:var(--black);text-transform:uppercase;letter-spacing:.5px}
.sec-title span{color:var(--red)}
.center{text-align:center;width:100%}
p.body{font-size:14px;line-height:28.5px;color:var(--text)}

/* header */
.site-header{height:81px;background:#fff}
.topbar{left:658px;top:0;width:437px;height:29px;background:var(--black);clip-path:polygon(3% 0,100% 0,97% 100%,0 100%);color:#fff;font-size:13px;display:flex;align-items:center;gap:24px;padding-left:22px}
.topbar .item{display:flex;align-items:center;gap:7px}
.brand{left:102px;top:16px;display:flex;align-items:center;gap:10px;font-size:16px;font-weight:600;letter-spacing:3px;color:var(--black)}
.brand .sq{width:16px;height:16px;background:var(--red)}
.main-nav{left:517px;top:45px;display:flex;gap:26px;font-size:13px;color:var(--black);letter-spacing:.4px}
.main-nav .active{color:var(--red)}
.header-rule{left:0;top:64px;width:1200px;height:17px;background:var(--red);clip-path:polygon(0 0,35% 60%,100% 100%,0 100%)}

/* hero */
.hero{height:460px;background:radial-gradient(ellipse at 38% 40%,#707070 0%,#4a4a4a 45%,#2e2e2e 100%)}
.hero-photo{left:490px;top:95px;width:710px;height:320px;background:radial-gradient(ellipse at 50% 55%,#2d4660 0%,#1c2c3e 55%,rgba(40,40,40,0) 75%)}
.hero-copy{left:101px;top:86px;font-size:31px;font-weight:700;line-height:40px;text-transform:uppercase}
.hero-copy .l1{color:var(--black)}
.hero-copy .l2{color:var(--red)}
.hero-copy .l3{color:var(--yellow)}
.hero-btns{left:101px;top:221px;display:flex;gap:4px}
.hero-btns .tag{width:146px;font-size:13px;padding:7px 0}
.hero-stripe{left:0;top:432px;width:1200px;height:28px;background:#fff;clip-path:polygon(0 100%,0 0,100% 100%)}
.hero-red{left:0;top:432px;width:1200px;height:19px;background:var(--red);clip-path:polygon(0 0,100% 60%,100% 100%,40% 55%)}

/* about */
.about{height:423px;background:#fff}
.about .sec-title{left:101px;top:72px}
.about p.body{left:101px;top:130px;width:525px;text-align:justify}
.about .tag{left:101px;top:336px;width:144px}
.about-frame{left:720px;top:93px;width:362px;height:291px;background:var(--red);clip-path:polygon(2% 0,100% 0,97% 100%,0 100%)}
.about-photo{left:708px;top:81px;width:363px;height:288px;background:linear-gradient(180deg,#5f8a3a 0%,#7aa04b 40%,#b9b79e 60%,#7a7a72 100%);clip-path:polygon(1% 0,100% 0,100% 100%,0 100%)}

/* features */
.features{height:441px;background:var(--grey)}
.features .diag{left:0;top:0;width:1200px;height:441px;background:#ecebeb;clip-path:polygon(20% 0,100% 0,100% 80%)}
.features .sec-title{top:52px}
.feature{top:155px;width:310px;text-align:center}
.feature .ico{height:58px;display:flex;justify-content:center;align-items:flex-end}
.feature h3{font-size:17px;font-weight:600;color:var(--red);letter-spacing:.5px;margin-top:10px}
.feature p{font-size:14px;line-height:28.5px;margin-top:14px}
.feature .tag{width:142px;margin-top:20px}

/* services */
.services{height:860px;background:#fff}
.services .sec-title{top:94px}
.service{width:296px}
.service h3{font-size:16.5px;font-weight:600;color:var(--black);letter-spacing:.3px}
.service .img{width:294px;height:117px;margin-top:12px}
.service p{font-size:14px;line-height:28.5px;margin-top:18px}
.service .tag{width:136px;margin-top:14px}

/* speciality */
.speciality{height:323px;background:var(--yellow)}
.spec-frame{left:114px;top:40px;width:505px;height:261px;background:var(--red);clip-path:polygon(0 0,100% 0,99% 100%,1% 100%)}
.spec-photo{left:104px;top:31px;width:498px;height:253px;background:radial-gradient(ellipse at 50% 65%,#8a8f96 0%,#2b2b2b 45%,#0c0c0c 100%)}
.speciality h3{left:680px;top:36px;font-size:17px;font-weight:600;color:var(--black);letter-spacing:.3px}
.speciality p.body{left:680px;top:80px;width:410px}
.speciality .tag{left:675px;top:230px;width:142px;font-size:13px}

/* gallery */
.gallery{height:368px;background:#fff}
.gallery .sec-title{top:58px}
.gal-row{left:0;top:140px;width:1200px;height:228px;display:flex}
.gal-row .g{flex:1;height:228px;position:relative}
.arrow{width:22px;height:22px;background:var(--red);display:flex;align-items:center;justify-content:center;top:260px}

/* reviews */
.reviews{height:428px;background:#fff}
.reviews .sec-title{top:46px}
.review{top:144px;width:314px;height:233px}
.review .box{position:absolute;left:0;top:0;width:100%;height:100%;border:2px solid var(--red);clip-path:polygon(0 0,100% 0,100% 100%,0 100%)}
.review .quote{position:absolute;left:10px;top:-38px;font-size:80px;font-weight:700;color:#f4a6a3;line-height:1;font-family:'Poppins',sans-serif;background:#fff;padding:0 4px;height:52px;overflow:hidden}
.review .avatar{position:absolute;left:22px;top:20px;width:64px;height:64px;border-radius:50%;background:linear-gradient(180deg,#c9d2dc,#8a9aae)}
.review .name{position:absolute;left:116px;top:30px;font-size:16px;font-weight:600;color:var(--red);letter-spacing:.3px}
.review .role{position:absolute;left:116px;top:56px;font-size:14px;color:#555}
.review p{position:absolute;left:22px;top:112px;width:282px;font-size:13px;line-height:28.5px}

/* contact */
.contact{height:607px;background:linear-gradient(100deg,#2a2a2a 0%,#141414 45%,#1d1d1d 70%,#3a3a3a 100%)}
.contact h2{top:38px;font-size:28px;font-weight:600;color:#fff;letter-spacing:1px}
.contact .sub{top:82px;font-size:13px;color:#fff}
.form-box{left:360px;top:132px;width:480px;height:475px;background:#c62a26}
.field{position:absolute;left:29px;width:420px;height:38px;background:#fff;font-size:14px;color:#444;padding:8px 18px}
.field.msg{height:97px}
.form-box .tag{position:absolute;left:183px;top:409px;width:116px;font-size:13px}

/* footer */
.site-footer{height:403px;background:#e8e8e8}
.foot-brand{left:0;top:48px;width:100%;display:flex;justify-content:center;align-items:center;gap:12px;font-size:17px;font-weight:600;letter-spacing:4px;color:var(--black)}
.foot-brand .sq{width:16px;height:16px;background:var(--red)}
.cbar{top:139px;height:53px;display:flex;align-items:center;gap:18px;font-size:14px}
.cbar .t{font-weight:600;font-size:15px;line-height:20px}
.cbar .v{font-size:14px;line-height:22px}
.cbar-black{left:0;width:421px;background:var(--black);color:#fff;padding-left:100px}
.cbar-red{left:438px;width:321px;background:var(--red);color:#fff;padding-left:18px}
.cbar-yellow{left:776px;width:424px;background:var(--yellow);color:#fff;padding-left:18px}
.foot-h{font-size:16px;font-weight:600;color:var(--red);letter-spacing:.5px}
.hours{left:428px;top:245px}
.hours .row{display:flex;align-items:center;gap:6px;font-size:14px;color:var(--black);margin-top:8px}
.follow{left:658px;top:245px}
.follow .row{display:flex;gap:6px;margin-top:8px}
.follow .dot{width:31px;height:31px;border-radius:50%;background:var(--black)}
.foot-nav{left:0;top:330px;width:100%;display:flex;justify-content:center;gap:24px;font-size:14px;color:var(--black)}
.copy{left:0;top:377px;width:100%;height:26px;background:var(--black);color:#fff;font-size:12px;text-align:center;line-height:26px}
</style>
</head>
<body>

<header class="site-header">
  <div class="abs brand"><span class="sq"></span>KESSLER RESTORATIONS</div>
  <div class="abs topbar">
    <span class="item"><svg width="14" height="14" viewBox="0 0 24 24"><path fill="#e8322b" d="M6.6 10.8a15 15 0 0 0 6.6 6.6l2.2-2.2a1 1 0 0 1 1-.25 11.4 11.4 0 0 0 3.6.6 1 1 0 0 1 1 1V20a1 1 0 0 1-1 1A17 17 0 0 1 3 4a1 1 0 0 1 1-1h3.5a1 1 0 0 1 1 1 11.4 11.4 0 0 0 .6 3.6 1 1 0 0 1-.25 1z"/></svg>+6205550147</span>
    <span class="item"><svg width="18" height="13" viewBox="0 0 18 13"><rect width="18" height="13" fill="#e8322b"/><path d="M1 1l8 6 8-6" stroke="#fff" stroke-width="1.5" fill="none"/></svg>kesslerrestoration@mail.com</span>
  </div>
  <nav class="abs main-nav"><span class="active">HOME</span><span>ABOUT</span><span>RESTORATIONS SERVICE</span><span>PORTFOLIO</span><span>BLOG</span><span>CONTACT</span></nav>
  <div class="abs header-rule"></div>
</header>

<section class="hero">
  <div class="ph hero-photo" role="img" aria-label="Classic dark blue German coupe, three-quarter front view"></div>
  <div class="abs hero-copy"><div class="l1">We are</div><div class="l2">Car restoration</div><div class="l3">company in California.</div></div>
  <div class="abs hero-btns"><span class="tag tag-red">CONTACT</span><span class="tag tag-black">PORTFOLIO</span></div>
  <div class="abs hero-stripe"></div>
  <div class="abs hero-red"></div>
</section>

<section class="about">
  <h2 class="abs sec-title"><span>About Kessler</span> Restoration</h2>
  <p class="abs body">Lorem Ipsum is simply dummy text of the printing and typesetting industry. Lorem Ipsum has been the industry's standard dummy text ever since the 1500s, when an unknown printer took a galley of type and scrambled it to make a type specimen book. It has survived not only five centuries, but also the leap into electronic typesetting, remaining essentially unchanged.</p>
  <span class="abs tag tag-yellow">READ MORE</span>
  <div class="abs about-frame"></div>
  <div class="ph about-photo" role="img" aria-label="Cream classic coupe parked on grass"></div>
</section>

<section class="features">
  <div class="abs diag"></div>
  <h2 class="abs sec-title center"><span>Our</span> Features</h2>
  <div class="abs feature" style="left:95px">
    <div class="ico"><svg width="54" height="54" viewBox="0 0 54 54" fill="none" stroke="#111" stroke-width="2"><circle cx="27" cy="32" r="14"/><circle cx="27" cy="32" r="8"/><circle cx="27" cy="32" r="3"/><path d="M27 6l2.5 5 5.5.8-4 3.9 1 5.5-5-2.6-5 2.6 1-5.5-4-3.9 5.5-.8z"/><path d="M10 12l1.5 3 3 .5-2.2 2 .5 3-2.8-1.5-2.8 1.5.5-3-2.2-2 3-.5zM44 12l1.5 3 3 .5-2.2 2 .5 3-2.8-1.5-2.8 1.5.5-3-2.2-2 3-.5z"/></svg></div>
    <h3>EXPERIENCED</h3>
    <p>Lorem Ipsum is simply dummy text of the printing and typesetting industry. Lorem Ipsum has</p>
    <span class="tag tag-yellow">READ MORE</span>
  </div>
  <div class="abs feature" style="left:446px">
    <div class="ico"><svg width="50" height="58" viewBox="0 0 50 58" fill="none" stroke="#111" stroke-width="2"><path d="M12 56V44C6 40 3 34 3 27 3 14 13 4 26 4s21 9 21 21c0 4-2 6-3 8l3 6h-4v7c0 2-2 4-4 4h-6v6"/><circle cx="24" cy="24" r="9"/><circle cx="24" cy="24" r="3"/><path d="M24 12v3M24 33v3M12 24h3M33 24h3M16 16l2 2M30 30l2 2M16 32l2-2M30 18l2-2"/></svg></div>
    <h3>CAPABLE</h3>
    <p>Lorem Ipsum is simply dummy text of the printing and typesetting industry. Lorem Ipsum has</p>
    <span class="tag tag-yellow">READ MORE</span>
  </div>
  <div class="abs feature" style="left:799px">
    <div class="ico"><svg width="46" height="46" viewBox="0 0 46 46" fill="none" stroke="#111" stroke-width="2"><rect x="3" y="20" width="9" height="23"/><path d="M12 22l8-10 2-9c4 0 6 3 5 8l-2 7h14c3 0 4 3 3 5l-4 16c-1 3-3 4-5 4H12"/></svg></div>
    <h3>PREPARED</h3>
    <p>Lorem Ipsum is simply dummy text of the printing and typesetting industry. Lorem Ipsum has</p>
    <span class="tag tag-yellow">READ MORE</span>
  </div>
</section>

<section class="services">
  <h2 class="abs sec-title center"><span>Restoration</span> Services</h2>

  <div class="abs service" style="left:102px;top:154px">
    <h3>MECHANICAL SERVICES</h3>
    <div class="img" role="img" aria-label="Close-up of a sports car wheel with red brake caliper" style="background:linear-gradient(135deg,#2a2a2a,#5a5a5a 50%,#1a1a1a)"></div>
    <p>Lorem Ipsum is simply dummy text of the printing and typesetting industry. Lorem Ipsum has</p>
    <span class="tag tag-yellow">READ MORE</span>
  </div>
  <div class="abs service" style="left:453px;top:154px">
    <h3>PAINTING &amp; FINISHING</h3>
    <div class="img" role="img" aria-label="Technician in protective suit spray painting a car panel" style="background:linear-gradient(135deg,#8a7a5c,#d9d4c8 55%,#a9a39a)"></div>
    <p>Lorem Ipsum is simply dummy text of the printing and typesetting industry. Lorem Ipsum has</p>
    <span class="tag tag-yellow">READ MORE</span>
  </div>
  <div class="abs service" style="left:803px;top:154px">
    <h3>PARTIAL RESTORATIONS</h3>
    <div class="img" role="img" aria-label="White classic beetle-style car in front of green hills" style="background:linear-gradient(180deg,#4f7a3a,#7e9a5e 45%,#c8c8c0 70%,#6c6c64)"></div>
    <p>Lorem Ipsum is simply dummy text of the printing and typesetting industry. Lorem Ipsum has</p>
    <span class="tag tag-yellow">READ MORE</span>
  </div>

  <div class="abs service" style="left:102px;top:503px">
    <h3>MECHANICAL UPGRADES</h3>
    <div class="img" role="img" aria-label="White car raised on a workshop lift" style="background:linear-gradient(135deg,#d8d8d8,#f2f2f2 50%,#9a9a9a)"></div>
    <p>Lorem Ipsum is simply dummy text of the printing and typesetting industry. Lorem Ipsum has</p>
    <span class="tag tag-yellow">READ MORE</span>
  </div>
  <div class="abs service" style="left:453px;top:503px">
    <h3>COLLECTOR SERVICES</h3>
    <div class="img" role="img" aria-label="Row of silver and blue classic sports cars" style="background:linear-gradient(180deg,#b6bcc4,#7d8794 50%,#3c6aa8 75%,#5a5a4a)"></div>
    <p>Lorem Ipsum is simply dummy text of the printing and typesetting industry. Lorem Ipsum has</p>
    <span class="tag tag-yellow">READ MORE</span>
  </div>
  <div class="abs service" style="left:803px;top:503px">
    <h3>ACCIDENT RESTORATION</h3>
    <div class="img" role="img" aria-label="Damaged orange sedan with crumpled front" style="background:linear-gradient(135deg,#7a6a50,#d99a3a 50%,#8a7a62)"></div>
    <p>Lorem Ipsum is simply dummy text of the printing and typesetting industry. Lorem Ipsum has</p>
    <span class="tag tag-yellow">READ MORE</span>
  </div>
</section>

<section class="speciality">
  <div class="abs spec-frame"></div>
  <div class="ph spec-photo" role="img" aria-label="Classic racing sports car in striped livery on a dark background"></div>
  <h3 class="abs">SPECIALITY VEHICLES</h3>
  <p class="abs body">Lorem Ipsum is simply dummy text of the printing and typesetting industry. Lorem Ipsum has Lorem Ipsum is simply dummy text of the printing and typesetting industry. Lorem Ipsum has</p>
  <span class="abs tag tag-black">READ MORE</span>
</section>

<section class="gallery">
  <h2 class="abs sec-title center"><span>Our</span> Gallery</h2>
  <div class="abs gal-row">
    <div class="g" role="img" aria-label="Cream classic coupe on grass" style="background:linear-gradient(180deg,#5f8a3a,#a8a890 60%,#6a6a62)"></div>
    <div class="g" role="img" aria-label="Silver and blue classic sports cars under cloudy sky" style="background:linear-gradient(180deg,#c4c8cc,#8a929c 55%,#3c6aa8 80%,#5a5a48)"></div>
    <div class="g" role="img" aria-label="Dark blue classic coupe in front of a glass building" style="background:linear-gradient(180deg,#6a6452,#c9a660 35%,#2d4660 70%,#3a3a36)"></div>
    <div class="g" role="img" aria-label="White classic beetle-style car with green hills" style="background:linear-gradient(180deg,#8fb0d0,#4f7a3a 40%,#c8c8c0 70%,#6c6c64)"></div>
  </div>
  <div class="abs arrow" style="left:102px"><svg width="8" height="10" viewBox="0 0 8 10"><path d="M8 0v10L0 5z" fill="#111"/></svg></div>
  <div class="abs arrow" style="left:1076px"><svg width="8" height="10" viewBox="0 0 8 10"><path d="M0 0v10l8-5z" fill="#111"/></svg></div>
</section>

<section class="reviews">
  <h2 class="abs sec-title center"><span>Recent</span> Reviews</h2>
  <div class="abs review" style="left:102px">
    <div class="box"></div><div class="quote">&ldquo;</div>
    <div class="avatar" role="img" aria-label="Reviewer portrait"></div>
    <div class="name">DAREN HOLT</div><div class="role">Teacher</div>
    <p>Lorem Ipsum is simply dummy text of the printing and typesetting industry. Lorem Ipsum has</p>
  </div>
  <div class="abs review" style="left:441px">
    <div class="box"></div><div class="quote">&ldquo;</div>
    <div class="avatar" role="img" aria-label="Reviewer portrait"></div>
    <div class="name">DAREN HOLT</div><div class="role">Teacher</div>
    <p>Lorem Ipsum is simply dummy text of the printing and typesetting industry. Lorem Ipsum has</p>
  </div>
  <div class="abs review" style="left:776px">
    <div class="box"></div><div class="quote">&ldquo;</div>
    <div class="avatar" role="img" aria-label="Reviewer portrait"></div>
    <div class="name">DAREN HOLT</div><div class="role">Teacher</div>
    <p>Lorem Ipsum is simply dummy text of the printing and typesetting industry. Lorem Ipsum has</p>
  </div>
</section>

<section class="contact" role="img" aria-label="Dimmed background of classic cars in a garage">
  <h2 class="abs center">GET IN TOUCH WITH US</h2>
  <div class="abs sub center">Lorem Ipsum is simply dummy text of the printing and typesetting industry</div>
  <div class="abs form-box">
    <div class="field" style="top:37px">Name</div>
    <div class="field" style="top:98px">Last Name</div>
    <div class="field" style="top:159px">Phone Number</div>
    <div class="field" style="top:220px">Email</div>
    <div class="field msg" style="top:280px">Your message Here</div>
    <span class="tag tag-black">SUBMIT</span>
  </div>
</section>

<footer class="site-footer">
  <div class="abs foot-brand"><span class="sq"></span>KESSLER RESTORATIONS</div>
  <div class="abs cbar cbar-black">
    <svg width="34" height="34" viewBox="0 0 24 24"><path fill="#fff" d="M6.6 10.8a15 15 0 0 0 6.6 6.6l2.2-2.2a1 1 0 0 1 1-.25 11.4 11.4 0 0 0 3.6.6 1 1 0 0 1 1 1V20a1 1 0 0 1-1 1A17 17 0 0 1 3 4a1 1 0 0 1 1-1h3.5a1 1 0 0 1 1 1 11.4 11.4 0 0 0 .6 3.6 1 1 0 0 1-.25 1z"/></svg>
    <div><div class="t">Call Us</div><div class="v">+6205550147</div></div>
  </div>
  <div class="abs cbar cbar-red">
    <svg width="46" height="32" viewBox="0 0 46 32" fill="none" stroke="#fff" stroke-width="2.5"><rect x="2" y="2" width="42" height="28"/><path d="M2 2l21 16L44 2M2 30l15-13M44 30L29 17"/></svg>
    <div><div class="t">Email Us</div><div class="v">kesslerrestoration@mail.com</div></div>
  </div>
  <div class="abs cbar cbar-yellow">
    <svg width="30" height="38" viewBox="0 0 24 32"><path fill="#fff" d="M12 0C5.4 0 0 5.4 0 12c0 9 12 20 12 20s12-11 12-20C24 5.4 18.6 0 12 0zm0 17a5 5 0 1 1 0-10 5 5 0 0 1 0 10z"/></svg>
    <div><div class="t">Our Location</div><div class="v">Marlow East ST.2040, Bali</div></div>
  </div>
  <div class="abs hours">
    <div class="foot-h">WORK HOURS</div>
    <div class="row"><svg width="28" height="28" viewBox="0 0 28 28"><circle cx="14" cy="14" r="13" fill="#111"/><circle cx="14" cy="14" r="9" fill="none" stroke="#fff" stroke-width="2"/><path d="M14 8v6l4 3" stroke="#fff" stroke-width="2" fill="none"/></svg>09:00 AM - 08:00 PM</div>
  </div>
  <div class="abs follow">
    <div class="foot-h">FOLLOW US</div>
    <div class="row"><span class="dot"></span><span class="dot"></span><span class="dot"></span></div>
  </div>
  <nav class="abs foot-nav"><span>Home</span><span>About</span><span>Restorations Service</span><span>Portfolio</span><span>Blog</span><span>Contact</span></nav>
  <div class="abs copy">Copyright © 2023 Kessler Restorations. All rights reserved.</div>
</footer>

</body>
</html>
```